Smart, intuitive SaaS software dashboard design

PactLoom is an innovative modern SaaS (software as a service) solution for contract and meeting management.

What we are looking for is fresh ideas for our dashboard. We do not need web coding or actionable wireframes now – but purely great design ideas from where to continue forward.

How should a modern web software dashboard look like? Fresh, intuitive, easy-to-use, and adaptable for responsive mobile designs. We hope that when the user logs into the service and sees the dashboard, he/she gets a good big picture of the current status of the most important documents of his/hers company.

To get to know the service and see the components, we kindly ask you to register to our service at www.pactloom-example.net and to utilize the free trial (30 days) so you can see the existing dashboard live. And also try out how it works. Might help you to get ideas how to improve it.

(The designer we will choose might be offered later on to design some other pages as well (contract view and edit pages, meeting page etc).)

You’ll find additional information in the attachment.

You’ll find more information of the company and the service also at www.pactloom-example.net

Target Market(s)

Global

Industry/Entity Type

Business Management

Number of Pages Required

1 page

Font styles to use
Sans Serif

Requirements
Must have
• 1) Clear design idea for us to iterate from, 2) Modern look and feel - elegant & bold at the same time - still with credibility in our target group. And 3) Suitable for dashboard usage - it should it a clear big picture for the user.
• UPDATE:
• Users should see most important things with one glance. Therefore we would like to see AT LEAST these items mentioned below on the first page.
• NOTE: if all these things are visible on the dashboard, the menu list is maybe not needed on the left. (And there might be some icons on the top header with needed settings/inbox features anyway.)
• NOTE2: as explained earlier, the design should be responsive i.e. work without modifications in PC, iPad and mobile (the areas/boxes would just rearrange themselves on top of each other.)
• -First area should be Documents, which would include different document categories: Contracts, Finance & Admin and HR
• -All different types of Meetings could be the next area (upcoming ones clearly visible with date and maybe description, time and location visible also).
• -Reminders and Activity Feed (they might also be together in top of each other, so that Reminder is visible first and Activity feed can be chosen from the tab.)
• -Virtual Datarooms (maybe 1-3 different ones with some analytics for each visible e.g. like usage/visits per day)
• Saved searches in very important list as users can save their most important searches. There are typically many of these, so at least 5 should be visible and then see all button (maybe even more could be visible if they fit on your design)
• My Latest is also important.
• (As explained, Action Required area is NOT needed anymore).
Nice to have
• Surprise us!
Should not have
• Please avoid the boring traditional legacy stuff and the common report dashboards.
• You do not need design a 100% mockup for the techie to continue with. The ideas count.

```html
<!DOCTYPE html>
<html lang="en">
<head>
<meta charset="utf-8">
<title>PactLoom Dashboard</title>
<link href="https://fonts.googleapis.com/css2?family=Roboto:wght@400;500;700&display=swap" rel="stylesheet">
<style>
:root{
  --navy:#333a4d;
  --navy-dark:#2e3446;
  --green:#76c700;
  --page:#eef0f4;
  --white:#ffffff;
  --line:#e1e3e8;
  --text:#333842;
  --muted:#6b6f78;
  --star:#f5a000;
  --red:#e8173b;
  --orange:#f6a040;
  --purple:#a43bc2;
  --bar-green:#1fc35f;
}
*{box-sizing:border-box;margin:0;padding:0}
html,body{width:1200px;height:753px;overflow:hidden}
body{font-family:'Roboto',Arial,sans-serif;background:var(--page);color:var(--text);position:relative;font-size:12px}
.abs{position:absolute}
svg{display:block}

/* top bar */
.topbar{left:0;top:0;width:1200px;height:56px;background:var(--white);border-bottom:1px solid var(--line)}
.brand{left:0;top:0;width:228px;height:56px;background:var(--navy);display:flex;align-items:center;padding-left:44px;gap:8px}
.brand-dot{width:22px;height:22px;border-radius:50%;background:var(--green)}
.brand-name{color:var(--white);font-size:18px;font-weight:400;letter-spacing:.5px}
.nav-item{top:0;height:56px;display:flex;align-items:center;gap:10px;padding-left:18px;border-right:1px solid var(--line);font-size:14px;color:var(--text)}
.user{left:1008px;top:0;width:192px;height:56px;border-left:1px solid var(--line);display:flex;align-items:center;padding-left:18px;gap:8px;font-size:14px;font-weight:500}
.avatar{border-radius:50%;background:radial-gradient(circle at 45% 40%,#d9a27c,#7a4a32 70%,#3b2419)}

/* second bar */
.subbar{left:0;top:56px;width:1200px;height:46px;background:var(--white);border-bottom:1px solid var(--line)}
.latest{left:0;top:56px;width:228px;height:46px;background:var(--green);color:var(--white);display:flex;align-items:center;padding-left:46px;gap:12px;font-size:15px;font-weight:500}
.saved{left:228px;top:56px;width:132px;height:46px;border-right:1px solid var(--line);display:flex;align-items:center;padding-left:15px;font-size:13px;font-weight:500}
.badge{position:absolute;left:101px;top:6px;width:14px;height:14px;border-radius:50%;background:var(--red);color:var(--white);font-size:8px;display:flex;align-items:center;justify-content:center}
.search{left:360px;top:56px;width:499px;height:46px;display:flex;align-items:center;padding-left:16px;font-size:13px;color:var(--muted)}
.select{top:56px;height:46px;border-left:1px solid var(--line);display:flex;align-items:center;justify-content:space-between;padding:0 20px 0 22px;font-size:13px}
.plus{left:1125px;top:56px;width:47px;height:46px;background:var(--green);display:flex;align-items:center;justify-content:center}

/* section headings */
.section-title{font-size:18px;font-weight:400;color:var(--text)}

/* category cards */
.card{top:167px;width:196px;height:227px;background:var(--white);border:1px solid #e4e6ea}
.card.active{border:2px solid var(--green)}
.card-icon{position:absolute;left:0;right:0;top:18px;display:flex;justify-content:center}
.card-rule{position:absolute;left:0;right:0;top:87px;height:1px;background:var(--line)}
.card-label{position:absolute;left:50%;top:76px;transform:translateX(-50%);width:85px;height:23px;border:1px solid #d2d5da;border-radius:12px;background:var(--white);font-size:13px;color:var(--muted);display:flex;align-items:center;justify-content:center}
.card-text{position:absolute;left:0;right:0;top:117px;text-align:center;font-size:11.5px;line-height:16px;color:#555a63}
.read-more{position:absolute;left:50%;top:155px;transform:translateX(-50%);height:21px;padding:0 8px;font-size:10px;color:#555a63;display:flex;align-items:center;white-space:nowrap;border:1px solid #d8dbe0;background:#f3f4f6}
.read-more.primary{background:var(--green);color:var(--white);border-color:var(--green)}
.read-more.plain{background:none;border:none}
.card-foot{position:absolute;left:0;right:0;bottom:0;height:33px;border-top:1px solid var(--line);display:flex;align-items:center;padding:0 9px;font-size:9px}
.stars{color:var(--star);font-size:13px;letter-spacing:-1px;flex:1}
.foot-sep{width:1px;height:10px;background:#c8cbd0;margin:0 6px}

/* meetings */
.meetings{left:45px;top:477px;width:807px;height:222px;background:var(--white);border:1px solid #e4e6ea}
.meeting{position:absolute;top:0;width:403px;height:220px}
.meeting + .meeting{border-left:1px solid #eceef1}
.photo{position:absolute;left:25px;top:33px;width:112px;height:112px;border-radius:50%}
.m-title{position:absolute;left:158px;top:36px;font-size:17px;font-weight:500;color:var(--text)}
.m-text{position:absolute;left:158px;top:62px;width:210px;font-size:13px;line-height:18px;color:var(--muted)}
.btn{position:absolute;top:126px;width:77px;height:26px;color:var(--white);font-size:13px;display:flex;align-items:center;justify-content:center}
.btn.green{left:155px;background:var(--green)}
.btn.dark{left:240px;background:var(--navy)}
.m-rule{position:absolute;left:25px;top:174px;width:333px;height:1px;background:#cfd2d7}
.m-info{position:absolute;left:27px;top:190px;display:flex;align-items:center;font-size:11.5px;color:var(--text);white-space:nowrap}
.m-info span{display:flex;align-items:center;gap:5px;margin-right:20px}

/* sidebar */
.sidebar{left:895px;top:102px;width:305px;height:651px;background:var(--navy)}
.tabs{left:928px;top:139px;width:235px;height:41px;border-bottom:1px solid #8a8f9c;display:flex}
.tab{height:41px;display:flex;align-items:center;justify-content:center;font-size:16px;color:var(--white)}
.tab.on{width:127px;border:1px solid #8a8f9c;border-bottom:none;color:var(--green);background:var(--navy-dark)}
.tab.off{width:108px}
.reminder{left:928px;width:235px;height:72px;border-bottom:1px solid #4a5062;display:flex;gap:12px}
.reminder .avatar{width:34px;height:34px;flex:none;margin-top:5px}
.r-title{color:var(--white);font-size:12px;font-weight:500;line-height:15px}
.r-date{color:var(--white);font-size:11.5px;margin-top:4px;display:flex;align-items:center;gap:5px}
.cal-btn{left:928px;top:432px;width:103px;height:28px;background:var(--white);display:flex;align-items:center;justify-content:center;gap:8px;font-size:11px;font-weight:700;color:var(--navy)}
.dataroom{left:928px;top:482px;width:232px;height:240px;background:var(--white)}
.dr-head{height:46px;background:var(--green);color:var(--white);font-size:16px;display:flex;align-items:center;padding-left:18px}
</style>
</head>
<body>

<!-- header -->
<div class="abs topbar"></div>
<div class="abs brand"><span class="brand-dot"></span><span class="brand-name">PactLoom</span></div>

<div class="abs nav-item" style="left:229px;width:131px">
  <svg width="24" height="24" viewBox="0 0 24 24"><circle cx="12" cy="12" r="8" fill="none" stroke="#333842" stroke-width="3" stroke-dasharray="3 2.3"/><circle cx="12" cy="12" r="6" fill="none" stroke="#333842" stroke-width="2"/><circle cx="12" cy="12" r="2.5" fill="none" stroke="#333842" stroke-width="1.6"/></svg>Settings
</div>
<div class="abs nav-item" style="left:360px;width:101px">
  <svg width="22" height="20" viewBox="0 0 22 20"><path d="M11 1v9M7 6l4 4 4-4" fill="none" stroke="#333842" stroke-width="2"/><path d="M1 11h6l1 3h6l1-3h6v8H1z" fill="#333842"/></svg>Inbox
</div>
<div class="abs nav-item" style="left:461px;width:120px">
  <svg width="22" height="20" viewBox="0 0 22 20"><g fill="#333842"><rect x="0" y="1" width="4" height="4"/><rect x="0" y="8" width="4" height="4"/><rect x="0" y="15" width="4" height="4"/><rect x="7" y="2" width="15" height="2"/><rect x="7" y="9" width="15" height="2"/><rect x="7" y="16" width="15" height="2"/></g></svg>Features
</div>
<div class="abs nav-item" style="left:581px;border-right:none">
  <svg width="18" height="12" viewBox="0 0 18 12"><path d="M1 6h16M5 2L1 6l4 4M13 2l4 4-4 4" fill="none" stroke="#333842" stroke-width="2"/></svg>Anyway
</div>
<div class="abs user">
  <div class="avatar" style="width:26px;height:26px" role="img" aria-label="User profile photo"></div>
  <span style="flex:1">PactLoom</span>
  <svg width="14" height="8" viewBox="0 0 14 8" style="margin-right:18px"><path d="M0 0h14L7 8z" fill="#555a63"/></svg>
</div>

<!-- sub bar -->
<div class="abs subbar"></div>
<div class="abs latest">
  <svg width="18" height="20" viewBox="0 0 18 20"><path d="M1 8h16v11H1z" fill="#fff"/><path d="M4 8V3h6l3 3v2" fill="none" stroke="#fff" stroke-width="1.6"/></svg>
  <span style="flex:1">My Latest</span>
  <svg width="14" height="8" viewBox="0 0 14 8" style="margin-right:8px"><path d="M0 0h14L7 8z" fill="#fff"/></svg>
</div>
<div class="abs saved">Saved searches<span class="badge">5</span></div>
<div class="abs search">Search..</div>
<div class="abs select" style="left:859px;width:120px">Category
  <svg width="11" height="7" viewBox="0 0 11 7"><path d="M1 1l4.5 4.5L10 1" fill="none" stroke="#333842" stroke-width="2"/></svg></div>
<div class="abs select" style="left:979px;width:146px;font-weight:500">CONTRACTS
  <svg width="11" height="7" viewBox="0 0 11 7"><path d="M1 1l4.5 4.5L10 1" fill="none" stroke="#333842" stroke-width="2"/></svg></div>
<div class="abs plus"><svg width="14" height="14" viewBox="0 0 14 14"><path d="M7 0v14M0 7h14" stroke="#fff" stroke-width="3"/></svg></div>

<!-- document categories -->
<div class="abs section-title" style="left:42px;top:132px">Document Categories</div>

<div class="abs card" style="left:43px">
  <div class="card-icon"><svg width="44" height="48" viewBox="0 0 44 48"><circle cx="18" cy="17" r="8" fill="#8e939c"/><path d="M4 46c0-11 6-16 14-16s14 5 14 16z" fill="#8e939c"/><path d="M24 2h12l6 6v18H24z" fill="#fff" stroke="#76c700" stroke-width="1.5"/><path d="M28 10h10M28 14h10M28 18h10" stroke="#76c700" stroke-width="1.2"/></svg></div>
  <div class="card-rule"></div><div class="card-label">Contracts</div>
  <div class="card-text">Lorem ipsum dolor sit amet<br>consectetur adcing elit,</div>
  <div class="read-more">Read More</div>
  <div class="card-foot"><span class="stars">★★★★★</span><svg width="10" height="10" viewBox="0 0 10 10"><path d="M1 2h4M1 2v7h7V5M4 6l5-5" fill="none" stroke="#555" stroke-width="1"/></svg><span class="foot-sep"></span>Total 36</div>
</div>

<div class="abs card active" style="left:248px">
  <div class="card-icon" style="top:17px"><svg width="44" height="48" viewBox="0 0 44 48"><circle cx="18" cy="17" r="8" fill="#333a4d"/><path d="M4 46c0-11 6-16 14-16s14 5 14 16z" fill="#333a4d"/><circle cx="33" cy="38" r="9" fill="#76c700"/><text x="33" y="42.5" text-anchor="middle" font-size="12" font-weight="700" fill="#fff" font-family="Roboto,sans-serif">$</text></svg></div>
  <div class="card-rule" style="top:86px"></div><div class="card-label" style="top:75px">Finance</div>
  <div class="card-text" style="top:116px">Lorem ipsum dolor sit amet<br>consectetur adcing elit,</div>
  <div class="read-more primary" style="top:154px">Read More</div>
  <div class="card-foot"><span class="stars">★★★★★</span><svg width="10" height="10" viewBox="0 0 10 10"><path d="M1 2h4M1 2v7h7V5M4 6l5-5" fill="none" stroke="#555" stroke-width="1"/></svg><span class="foot-sep"></span>Total 36</div>
</div>

<div class="abs card" style="left:453px">
  <div class="card-icon"><svg width="44" height="48" viewBox="0 0 44 48"><circle cx="22" cy="17" r="9" fill="#8e939c"/><path d="M4 46c0-11 7-16 18-16s18 5 18 16z" fill="#8e939c"/><path d="M18 30l4 6 4-6z" fill="#76c700"/></svg></div>
  <div class="card-rule"></div><div class="card-label">Admin</div>
  <div class="card-text">Lorem ipsum dolor sit amet<br>consectetur adcing elit,</div>
  <div class="read-more plain">Read More</div>
  <div class="card-foot"><span class="stars">★★★★★</span><svg width="10" height="10" viewBox="0 0 10 10"><path d="M1 2h4M1 2v7h7V5M4 6l5-5" fill="none" stroke="#555" stroke-width="1"/></svg><span class="foot-sep"></span>Total 36</div>
</div>

<div class="abs card" style="left:657px">
  <div class="card-icon"><svg width="44" height="48" viewBox="0 0 44 48"><circle cx="20" cy="17" r="9" fill="#8e939c"/><path d="M6 46c0-11 5-16 14-16s14 5 14 16z" fill="#8e939c"/><circle cx="32" cy="38" r="8" fill="#8ed23a" stroke="#fff" stroke-width="2"/><path d="M32 42l-3.5-3.5a2 2 0 013.5-2 2 2 0 013.5 2z" fill="#fff"/></svg></div>
  <div class="card-rule"></div><div class="card-label">HR</div>
  <div class="card-text">Lorem ipsum dolor sit amet<br>consectetur adcing elit,</div>
  <div class="read-more">Read More</div>
  <div class="card-foot"><span class="stars">★★★★★</span><svg width="10" height="10" viewBox="0 0 10 10"><path d="M1 2h4M1 2v7h7V5M4 6l5-5" fill="none" stroke="#555" stroke-width="1"/></svg><span class="foot-sep"></span>Total 36</div>
</div>

<!-- upcoming meetings -->
<div class="abs section-title" style="left:49px;top:434px">Upcoming Meetings</div>
<div class="abs meetings">
  <div class="meeting" style="left:0">
    <div class="photo" role="img" aria-label="Portrait photo of meeting host" style="background:radial-gradient(circle at 50% 45%,#c9a58c,#6d7f92 70%,#3d4d5e)"></div>
    <div class="m-title">Board Meetings</div>
    <div class="m-text">Lorem Ipsum is simply dummy text of the prining and typesetting indus-try. Lorem &nbsp;Ipsum is simply.</div>
    <div class="btn green">See All</div><div class="btn dark">ADD</div>
    <div class="m-rule"></div>
    <div class="m-info">
      <span><svg width="11" height="11" viewBox="0 0 11 11"><rect x=".5" y="1.5" width="10" height="9" fill="none" stroke="#444" /><path d="M.5 4h10M3 0v3M8 0v3" stroke="#444"/></svg>17 Jun 2016</span>
      <span><svg width="13" height="13" viewBox="0 0 13 13"><circle cx="6.5" cy="6.5" r="5.5" fill="none" stroke="#444" stroke-width="1.3"/><path d="M6.5 3v4h3" fill="none" stroke="#444" stroke-width="1.3"/></svg>3:20pm</span>
      <span><svg width="10" height="13" viewBox="0 0 10 13"><path d="M5 12S1 7 1 5a4 4 0 018 0c0 2-4 7-4 7z" fill="none" stroke="#444" stroke-width="1.3"/><circle cx="5" cy="5" r="1.4" fill="#444"/></svg>Harbor Lane 2-4(Vantix.)</span>
    </div>
  </div>
  <div class="meeting" style="left:403px">
    <div class="photo" role="img" aria-label="Portrait photo of meeting host" style="background:radial-gradient(circle at 50% 45%,#d3a58a,#6e4a3b 70%,#c9c6c4)"></div>
    <div class="m-title">Board Meetings</div>
    <div class="m-text">Lorem Ipsum is simply dummy text of the prining and typesetting indus-try. Lorem &nbsp;Ipsum is simply.</div>
    <div class="btn green">See All</div><div class="btn dark">ADD</div>
    <div class="m-rule"></div>
    <div class="m-info">
      <span><svg width="11" height="11" viewBox="0 0 11 11"><rect x=".5" y="1.5" width="10" height="9" fill="none" stroke="#444" /><path d="M.5 4h10M3 0v3M8 0v3" stroke="#444"/></svg>16 Agu 2016</span>
      <span><svg width="13" height="13" viewBox="0 0 13 13"><circle cx="6.5" cy="6.5" r="5.5" fill="none" stroke="#444" stroke-width="1.3"/><path d="M6.5 3v4h3" fill="none" stroke="#444" stroke-width="1.3"/></svg>3:20pm</span>
      <span><svg width="10" height="13" viewBox="0 0 10 13"><path d="M5 12S1 7 1 5a4 4 0 018 0c0 2-4 7-4 7z" fill="none" stroke="#444" stroke-width="1.3"/><circle cx="5" cy="5" r="1.4" fill="#444"/></svg>Harbor Lane 2-4(Vantix.)</span>
    </div>
  </div>
</div>

<!-- sidebar -->
<div class="abs sidebar"></div>
<div class="abs tabs"><div class="tab on">Remindres</div><div class="tab off">Activty Feed</div></div>

<div class="abs reminder" style="top:192px">
  <div class="avatar" role="img" aria-label="Contact photo"></div>
  <div><div class="r-title">Price evaluation point:- Mareting<br>Co-operation Agreement Adsolve Ltd</div>
  <div class="r-date"><svg width="10" height="10" viewBox="0 0 11 11"><rect x=".5" y="1.5" width="10" height="9" fill="#fff"/><path d="M.5 4h10" stroke="#333a4d"/></svg>29-6-2016</div></div>
</div>
<div class="abs reminder" style="top:269px">
  <div class="avatar" role="img" aria-label="Contact photo" style="margin-left:4px"></div>
  <div><div class="r-title">Expiring:- Security services for<br>Lakeside Rock event 2016</div>
  <div class="r-date"><svg width="10" height="10" viewBox="0 0 11 11"><rect x=".5" y="1.5" width="10" height="9" fill="#fff"/><path d="M.5 4h10" stroke="#333a4d"/></svg>1-7-2016</div></div>
</div>
<div class="abs reminder" style="top:349px">
  <div class="avatar" role="img" aria-label="Contact photo"></div>
  <div><div class="r-title">Expiring:-Cleaning Services<br>Areement 2015</div>
  <div class="r-date"><svg width="10" height="10" viewBox="0 0 11 11"><rect x=".5" y="1.5" width="10" height="9" fill="#fff"/><path d="M.5 4h10" stroke="#333a4d"/></svg>6-7-2016</div></div>
</div>

<div class="abs cal-btn"><svg width="11" height="11" viewBox="0 0 11 11"><rect x=".5" y="1.5" width="10" height="9" fill="none" stroke="#333a4d"/><path d="M.5 4h10M3 0v3M8 0v3" stroke="#333a4d"/></svg>CAIENDAR</div>

<div class="abs dataroom">
  <div class="dr-head">Virtual Datarooms</div>
  <svg width="232" height="194" viewBox="0 0 232 194" font-family="Roboto,sans-serif" font-size="7" fill="#888">
    <circle cx="48" cy="19" r="2.5" fill="var(--bar-green)"/><text x="56" y="22">Corvia</text>
    <circle cx="105" cy="19" r="2.5" fill="var(--orange)"/><text x="113" y="22">Bexel</text>
    <circle cx="152" cy="19" r="2.5" fill="var(--purple)"/><text x="160" y="22">Yarrow</text>
    <g stroke="#e3e5e8" stroke-dasharray="2 2">
      <line x1="42" y1="52" x2="222" y2="52"/><line x1="42" y1="73.6" x2="222" y2="73.6"/>
      <line x1="42" y1="95.2" x2="222" y2="95.2"/><line x1="42" y1="116.8" x2="222" y2="116.8"/>
      <line x1="42" y1="138.4" x2="222" y2="138.4"/>
    </g>
    <line x1="42" y1="160" x2="222" y2="160" stroke="#ccc"/>
    <g text-anchor="end"><text x="36" y="54">500</text><text x="36" y="76">400</text><text x="36" y="97">300</text><text x="36" y="119">200</text><text x="36" y="140">100</text><text x="36" y="162">0</text></g>
    <!-- bars: scale 0.216 px per unit -->
    <g>
      <rect x="46" y="135.2" width="16" height="24.8" fill="var(--purple)"/><rect x="46" y="122.2" width="16" height="13" fill="var(--orange)"/><rect x="46" y="79" width="16" height="43.2" fill="var(--bar-green)"/>
      <rect x="71" y="123.3" width="16" height="36.7" fill="var(--purple)"/><rect x="71" y="98.5" width="16" height="24.8" fill="var(--orange)"/><rect x="71" y="68.2" width="16" height="30.3" fill="var(--bar-green)"/>
      <rect x="95" y="135.2" width="16" height="24.8" fill="var(--purple)"/><rect x="95" y="122.2" width="16" height="13" fill="var(--orange)"/><rect x="95" y="92" width="16" height="30.2" fill="var(--bar-green)"/>
      <rect x="120" y="129.8" width="16" height="30.2" fill="var(--purple)"/><rect x="120" y="110.4" width="16" height="19.4" fill="var(--orange)"/><rect x="120" y="98.5" width="16" height="11.9" fill="var(--bar-green)"/>
      <rect x="144" y="116.8" width="16" height="43.2" fill="var(--purple)"/><rect x="144" y="92" width="16" height="24.8" fill="var(--orange)"/><rect x="144" y="55.2" width="16" height="36.8" fill="var(--bar-green)"/>
      <rect x="169" y="128.7" width="16" height="31.3" fill="var(--purple)"/><rect x="169" y="115.7" width="16" height="13" fill="var(--orange)"/><rect x="169" y="79" width="16" height="36.7" fill="var(--bar-green)"/>
      <rect x="193" y="123.3" width="16" height="36.7" fill="var(--purple)"/><rect x="193" y="98.5" width="16" height="24.8" fill="var(--orange)"/><rect x="193" y="68.2" width="16" height="30.3" fill="var(--bar-green)"/>
    </g>
    <g text-anchor="middle"><text x="54" y="176">Mon</text><text x="79" y="176">Tue</text><text x="103" y="176">Wed</text><text x="128" y="176">Thu</text><text x="152" y="176">Fri</text><text x="177" y="176">Sat</text><text x="201" y="176">Sun</text></g>
  </svg>
</div>

</body>
</html>
```